IT Company based on Biology Business Needs a Business Card Design

We need a business card design for a new company called 'Lumen CELL'. We develop the machine learning solutions especially focused on deep learning algorithms for biology industry. Our initial product is a vision detection on biological images to help doctors diagnose the symptoms. We would like to see designs that use the color green.

Industry/Entity Type

Business

```html
<!DOCTYPE html>
<html lang="en">
<head>
<meta charset="utf-8">
<title>Lumen CELL – Business Card</title>
<link href="https://fonts.googleapis.com/css2?family=Questrial&family=Montserrat:wght@600&display=swap" rel="stylesheet">
<style>
  :root {
    --backdrop: #1c1c1c;
    --paper: #f4f4f2;
    --green-light: #66a023;
    --green-dark: #1b7a3b;
    --ink: #333333;
    --white: #ffffff;
  }
  * { margin: 0; padding: 0; box-sizing: border-box; }
  html, body {
    width: 1200px; height: 1001px; overflow: hidden;
    background: var(--backdrop);
    font-family: "Questrial", "Century Gothic", sans-serif;
  }
  .card {
    position: absolute;
    left: 306px;
    width: 589px; height: 329px;
    background: var(--paper);
  }
  .card--front { top: 143px; }
  .card--back { top: 550px; }

  .holder { position: absolute; left: 38px; top: 70px; }
  .holder__name {
    font-family: "Montserrat", sans-serif; font-weight: 600;
    font-size: 18px; letter-spacing: 0.3px; color: var(--green-light);
    text-transform: uppercase;
  }
  .holder__title { font-size: 14px; color: var(--ink); margin-top: 2px; }

  .brand {
    position: absolute; display: flex; align-items: center; gap: 10px;
  }
  .brand__dot { width: 16px; height: 16px; border-radius: 50%; background: var(--green-dark); }
  .brand__name {
    font-family: "Questrial", sans-serif; font-size: 40px; letter-spacing: -1.5px;
    color: var(--green-light); line-height: 1; white-space: nowrap;
  }
  .card--front .brand { right: 37px; top: 73px; }

  .contact { position: absolute; left: 38px; top: 197px; list-style: none; }
  .contact__item {
    display: flex; align-items: center; gap: 9px;
    font-size: 14px; color: var(--ink); height: 19px;
  }
  .contact__icon { width: 14px; height: 14px; flex: none; }

  .address {
    position: absolute; right: 37px; top: 216px;
    text-align: right; font-size: 14px; line-height: 19px; color: var(--ink);
  }

  .band { position: absolute; left: 0; right: 0; top: 279px; height: 27px; display: flex; }
  .band__dark { width: 286px; background: var(--green-dark); display: flex; align-items: center; padding-left: 38px; }
  .band__light { flex: 1; background: var(--green-light); }
  .band__url { font-size: 14px; color: var(--white); }
  .band__url b { font-weight: normal; color: #8cc63f; }
  .band__dot {
    position: absolute; left: 274px; top: 1.5px;
    width: 24px; height: 24px; border-radius: 50%; background: var(--paper);
  }

  .card--back .brand { right: 65px; top: 223px; }
  .card--back .brand__name { font-size: 44px; }
  .back__url {
    position: absolute; right: 65px; top: 265px;
    font-size: 14px; color: var(--green-dark);
  }
  .back__url b { font-weight: normal; color: var(--green-light); }
</style>
</head>
<body>
  <section class="card card--front">
    <div class="holder">
      <p class="holder__name">Mara Ellison</p>
      <p class="holder__title">General Manager</p>
    </div>

    <div class="brand">
      <span class="brand__dot"></span>
      <span class="brand__name">Lumen CELL</span>
    </div>

    <ul class="contact">
      <li class="contact__item">
        <svg class="contact__icon" viewBox="0 0 14 14" aria-hidden="true">
          <rect width="14" height="14" rx="2" fill="var(--green-light)"/>
          <path d="M4 3.2c.5-.4 1-.3 1.3.2l.7 1.2c.2.4.1.8-.2 1l-.5.4c.4 1 1.1 1.7 2 2.2l.4-.5c.3-.3.7-.4 1-.2l1.2.7c.5.3.6.8.2 1.3-.6.8-1.5 1-2.4.6C5.7 9.3 4.5 8 3.8 6.3c-.4-1-.4-2.4.2-3.1z" fill="#fff"/>
        </svg>
        (555) 014-2290
      </li>
      <li class="contact__item">
        <svg class="contact__icon" viewBox="0 0 14 14" aria-hidden="true">
          <rect width="14" height="14" rx="2" fill="var(--green-light)"/>
          <rect x="4.5" y="2.5" width="5" height="3" fill="none" stroke="#fff" stroke-width="1"/>
          <rect x="2.5" y="5.5" width="9" height="4" rx="0.6" fill="#fff"/>
          <rect x="4.5" y="8.5" width="5" height="3" fill="#fff" stroke="var(--green-light)" stroke-width="0.8"/>
        </svg>
        (555) 014-2290
      </li>
      <li class="contact__item">
        <svg class="contact__icon" viewBox="0 0 14 14" aria-hidden="true">
          <rect width="14" height="14" rx="2" fill="var(--green-light)"/>
          <rect x="2.5" y="4" width="9" height="6" fill="none" stroke="#fff" stroke-width="1"/>
          <path d="M2.5 4l4.5 3.5L11.5 4M2.5 10l3.2-3M11.5 10L8.3 7" fill="none" stroke="#fff" stroke-width="0.9"/>
        </svg>
        info@lumencell.com
      </li>
    </ul>

    <address class="address" style="font-style:normal">
      48 Alder Creek Lane<br>Fairmont, NJ 07990
    </address>

    <div class="band">
      <div class="band__dark"><span class="band__url">www.<b>lumencell</b>.com</span></div>
      <div class="band__light"></div>
      <span class="band__dot"></span>
    </div>
  </section>

  <section class="card card--back">
    <div class="brand">
      <span class="brand__name">Lumen CELL</span>
    </div>
    <p class="back__url">www.<b>lumencell</b>.com</p>
  </section>
</body>
</html>
```